qLM Builders
Nimble Site Crafting
draft #229 - This looks pretty good. We prefer option 2 for the stationary. Clean and simple. We aren't so sure about the colored watermark. Seems like too much maybe
draft #223 - We really like the back of this one!
The contests has been extended for 3 more days. Please submit new designs. Due to the short time frame, we will only be accepting and rating full designs including complete stationary.
I will make every effort to provide feedback as soon as possible on designs concepts. Thank!
draft #96 - I like the back! The front is a little cookie cutter. Can you try something that integrates the "X" into the design. I don't really like the text all centered (draft #95,draft #94)
draft #102 I don't like the graphic at the top, but I like the back and I like how you integrated the X on the front like a watermark. can you remove that and add some icon's for phone,email, ect?
Some design inspiration - here are some cards we like
http://www.cardmarket.example/theme_previews/1778907-stylish-business-card?index=4
http://cardmarket.example/item/royal-modern-business-card/2484567?WT.ac=category_thumb&WT.seg_1=category_thumb&WT.z_author=omar-lindqvest
http://cardmarket.example/item/awesomeness-business-card/55256?WT.ac=category_thumb&WT.seg_1=category_thumb&WT.z_author=Bram
http://cardmarket.example/item/qr-business-card/1361513?WT.ac=category_thumb&WT.seg_1=category_thumb&WT.z_author=Marisk
http://cardmarket.example/item/clean-modern-business-card/1922436?WT.ac=category_thumb&WT.seg_1=category_thumb&WT.z_author=dustwick
http://cardmarket.example/theme_previews/1492534-neat-corporate-business-card?index=9
http://cardmarket.example/item/red-business-card/504464?WT.ac=category_thumb&WT.seg_1=category_thumb&WT.z_author=lumenpress
Also meant to mention, we prefer square cards (instead of the rounded corners).
If you have ideas for texture/embossing that would look nice please include! We are digging the glossy look on the back of some of these. But any details that help make the card unique is great!
thanks again!
Hi Designers. We got backed up and haven't been able to provide feedback yet.
There are also A LOT of designs to go through. We will be eliminating design's I consider "cookie cutter" templates. We are interested in unique designs that integrate the with the look and feel of the logo, or directly integrate parts of the logo with the designs.
In General, the Wavy/curvy look isn't what we are going for (there are A LOT of those).
There are some very unique integrations with the "X" that we like, especially when it's used kinda like a watermark.
We don't want any contact info on the back other then maybe the website.
Again thanks for your work! We will be sending specific feedback for the designs we like via PM in the next few hours.
Gavin@qlmbuilders
Thanks for all the designs and the note. We will be going through and selecting the few our favorite designs so far and offering tomorrow.
Thanks for the good work!
@PH - we will develop stationery for the liked business cards. Please let me know via private message. Thanks
sir please check pvt message top right side please
Note to Designers - This a a business Card & Stationary project. Designs should include concepts for both. Any questions or concerns please message me.

```html
<!DOCTYPE html>
<html lang="en">
<head>
<meta charset="utf-8">
<title>qLM Builders — Stationery Set</title>
<link href="https://fonts.googleapis.com/css2?family=Open+Sans:wght@400;600;700&display=swap" rel="stylesheet">
<style>
  :root {
    --blue: #29abe2;
    --ink: #1d1d1f;
    --grey: #8a8f94;
    --rule: #c9ccd0;
    --paper: #ffffff;
    --stage: #ffffff;
  }
  * { box-sizing: border-box; margin: 0; padding: 0; }
  html, body { width: 1200px; height: 482px; overflow: hidden; background: var(--stage); }
  body { position: relative; font-family: "Open Sans", Arial, sans-serif; color: var(--ink); }

  .sheet {
    position: absolute;
    background: var(--paper);
    box-shadow: 0 2px 6px rgba(0,0,0,.28);
    overflow: hidden;
  }
  .letterhead-fax { left: 19px; top: 36px; width: 312px; height: 408px; }
  .envelope-front { left: 391px; top: 53px; width: 370px; height: 187px; }
  .envelope-back { left: 391px; top: 259px; width: 370px; height: 185px; }
  .letterhead-plain { left: 787px; top: 36px; width: 305px; height: 408px; }
  .card-front { left: 1032px; top: 96px; width: 144px; height: 84px; z-index: 2; }
  .card-back { left: 1032px; top: 216px; width: 144px; height: 89px; z-index: 2; }

  .brand { position: absolute; line-height: 1; }
  .brand-name { display: block; font-weight: 700; color: var(--ink); letter-spacing: .2px; }
  .brand-tagline { display: block; font-weight: 400; color: var(--grey); margin-top: 2px; }
  .letterhead-fax .brand, .letterhead-plain .brand { left: 14px; top: 12px; }
  .letterhead-fax .brand-name, .letterhead-plain .brand-name { font-size: 15px; }
  .letterhead-fax .brand-tagline, .letterhead-plain .brand-tagline { font-size: 6px; }
  .envelope-front .brand { left: 16px; top: 14px; }
  .envelope-front .brand-name { font-size: 17px; }
  .envelope-front .brand-tagline { font-size: 6.5px; }
  .card-front .brand { left: 8px; top: 8px; }
  .card-front .brand-name { font-size: 8px; }
  .card-front .brand-tagline { font-size: 3.5px; }

  .center-name {
    position: absolute; left: 0; right: 0; text-align: center;
    font-weight: 700; color: var(--ink);
  }
  .envelope-back .center-name { top: 92px; font-size: 13px; }
  .card-back .center-name { top: 38px; font-size: 10px; }

  .band {
    position: absolute; left: 0; right: 0;
    background: var(--blue); color: #fff;
    font-size: 4.5px; line-height: 1.5; padding: 4px 10px;
  }
  .letterhead-fax .band, .letterhead-plain .band { bottom: 16px; height: 22px; }
  .envelope-front .band { bottom: 32px; height: 20px; }
  .card-front .band { bottom: 10px; height: 10px; padding: 1.5px 6px; font-size: 2.6px; }

  .corner { position: absolute; right: 0; }
  .letterhead-fax .corner, .letterhead-plain .corner { bottom: 16px; width: 44px; height: 36px; }
  .envelope-front .corner { bottom: 32px; width: 42px; height: 34px; }
  .card-front .corner { bottom: 10px; width: 18px; height: 16px; }

  .fax-form { position: absolute; left: 16px; top: 60px; width: 280px; }
  .fax-fields { display: grid; grid-template-columns: 1fr 1fr; column-gap: 18px; row-gap: 9px; }
  .fax-field { display: flex; align-items: flex-end; font-size: 6px; color: var(--ink); }
  .fax-field span { width: 30px; }
  .fax-field i { flex: 1; border-bottom: 1px solid var(--rule); height: 6px; }
  .fax-options { display: flex; justify-content: space-between; margin-top: 20px; font-size: 5.5px; }
  .fax-option { display: flex; align-items: center; gap: 3px; }
  .fax-option b { width: 6px; height: 6px; border: 1px solid var(--ink); }

  .contact-line { font-size: 3.4px; color: var(--ink); position: absolute; left: 8px; }
  .card-front .contact-name { top: 34px; font-size: 5px; font-weight: 600; }
  .card-front .contact-title { top: 41px; color: var(--grey); }
  .card-front .contact-info { top: 50px; line-height: 1.5; }

  .flap { position: absolute; inset: 0; }
</style>
</head>
<body>

  <section class="sheet letterhead-fax">
    <div class="brand"><span class="brand-name">qLM Builders</span><span class="brand-tagline">Nimble Site Crafting</span></div>
    <div class="fax-form">
      <div class="fax-fields">
        <div class="fax-field"><span>To:</span><i></i></div>
        <div class="fax-field"><span>From:</span><i></i></div>
        <div class="fax-field"><span>Fax:</span><i></i></div>
        <div class="fax-field"><span>Pages:</span><i></i></div>
        <div class="fax-field"><span>Phone:</span><i></i></div>
        <div class="fax-field"><span>Date:</span><i></i></div>
        <div class="fax-field"><span>Re:</span><i></i></div>
        <div class="fax-field"><span>CC:</span><i></i></div>
      </div>
      <div class="fax-options">
        <div class="fax-option"><b></b>Urgent</div>
        <div class="fax-option"><b></b>For Review</div>
        <div class="fax-option"><b></b>Please Comment</div>
        <div class="fax-option"><b></b>Please Reply</div>
        <div class="fax-option"><b></b>Please Recycle</div>
      </div>
    </div>
    <div class="band">48 Harbor Lane, Fairview, OR 97000 · Phone 555.014.2290<br>hello@qlmbuilders.example · www.qlmbuilders.example</div>
    <svg class="corner" viewBox="0 0 44 36" preserveAspectRatio="none"><polygon points="6,36 36,0 44,0 44,2 16,36" fill="#fff"/><polygon points="16,36 44,2 44,12 24,36" fill="#1d1d1f"/><polygon points="24,36 44,12 44,36" fill="#29abe2"/></svg>
  </section>

  <section class="sheet envelope-front">
    <div class="brand"><span class="brand-name">qLM Builders</span><span class="brand-tagline">Nimble Site Crafting</span></div>
    <div class="band">48 Harbor Lane, Fairview, OR 97000 · Phone 555.014.2290<br>hello@qlmbuilders.example · www.qlmbuilders.example</div>
    <svg class="corner" viewBox="0 0 44 36" preserveAspectRatio="none"><polygon points="6,36 36,0 44,0 44,2 16,36" fill="#fff"/><polygon points="16,36 44,2 44,12 24,36" fill="#1d1d1f"/><polygon points="24,36 44,12 44,36" fill="#29abe2"/></svg>
  </section>

  <section class="sheet envelope-back">
    <svg class="flap" viewBox="0 0 370 185" preserveAspectRatio="none"><polyline points="0,2 150,60 220,60 370,2" fill="none" stroke="#c9ccd0" stroke-width="1"/><polyline points="0,185 185,95 370,185" fill="none" stroke="#e2e4e6" stroke-width="1"/></svg>
    <div class="center-name">qLM Builders</div>
  </section>

  <section class="sheet letterhead-plain">
    <div class="brand"><span class="brand-name">qLM Builders</span><span class="brand-tagline">Nimble Site Crafting</span></div>
    <div class="band">48 Harbor Lane, Fairview, OR 97000 · Phone 555.014.2290<br>hello@qlmbuilders.example · www.qlmbuilders.example</div>
    <svg class="corner" viewBox="0 0 44 36" preserveAspectRatio="none"><polygon points="6,36 36,0 44,0 44,2 16,36" fill="#fff"/><polygon points="16,36 44,2 44,12 24,36" fill="#1d1d1f"/><polygon points="24,36 44,12 44,36" fill="#29abe2"/></svg>
  </section>

  <section class="sheet card-front">
    <div class="brand"><span class="brand-name">qLM Builders</span><span class="brand-tagline">Nimble Site Crafting</span></div>
    <div class="contact-line contact-name">Gavin Reyes</div>
    <div class="contact-line contact-title">Lead Web Developer</div>
    <div class="contact-line contact-info">Phone 555.014.2290<br>Gavin@qlmbuilders.example</div>
    <div class="band">www.qlmbuilders.example</div>
    <svg class="corner" viewBox="0 0 44 36" preserveAspectRatio="none"><polygon points="6,36 36,0 44,0 44,2 16,36" fill="#fff"/><polygon points="16,36 44,2 44,12 24,36" fill="#1d1d1f"/><polygon points="24,36 44,12 44,36" fill="#29abe2"/></svg>
  </section>

  <section class="sheet card-back">
    <div class="center-name">qLM Builders</div>
  </section>

</body>
</html>
```